Webdesign Metall- und Stahlbau Harkenfeld GmbH
Zielgruppe
Metall- und Stahlbau Harkenfeld GmbH
Zielgruppe: öffentlicher Bereich, Industrie, Gesundheitswesen > deutschlandweit tätig
Aufgabenstellung
keine bewegten Bilder oder Elemente in der Website
klassisches Layout
sehr konservativ

```html
<!DOCTYPE html>
<html lang="de">
<head>
<meta charset="utf-8">
<title>Metall- und Stahlbau Harkenfeld GmbH</title>
<link href="https://fonts.googleapis.com/css2?family=Arimo:wght@400;700&display=swap" rel="stylesheet">
<style>
  :root{
    --yellow:#ffcb3b;
    --yellow-light:#ffdc50;
    --blue:#0707b8;
    --ink:#1d1d1d;
    --white:#ffffff;
    --footer:#2a2a2a;
  }
  *{margin:0;padding:0;box-sizing:border-box}
  html,body{width:796px;height:1200px;overflow:hidden;background:var(--white)}
  body{position:relative;font-family:"Arimo",Arial,sans-serif;color:var(--ink)}
  .abs{position:absolute}

  .site-header{left:0;top:0;width:796px;height:47px;background:var(--yellow)}
  .brand{left:124px;top:7px;display:flex;align-items:flex-start;gap:6px}
  .brand-square{width:33px;height:33px;background:var(--blue)}
  .brand-name{color:var(--blue);font-size:11px;line-height:12px;font-weight:400;width:115px}
  .brand-claim{left:163px;top:34px;font-size:5.3px;color:var(--blue)}
  .main-nav{left:309px;top:20px;display:flex;gap:3px;font-size:6.7px;font-weight:700;white-space:nowrap}
  .main-nav .active{color:var(--blue)}
  .nav-marker{left:306px;top:44px;width:25px;height:3px;background:var(--blue)}

  .hero{left:0;top:47px;width:796px;height:327px;
    background:linear-gradient(180deg,#5d6b4a 0%,#8a8c7a 8%,#c7ccd6 22%,#9aa6b8 45%,#a79d92 70%,#b88f67 100%)}
  .contact-pill{height:24px;border-radius:12px;background:var(--white);display:flex;align-items:center;gap:8px;padding-left:13px;font-size:7px;font-weight:700;top:252px;white-space:nowrap}
  .contact-pill svg{width:12px;height:12px;fill:var(--blue);flex:none}

  .welcome-panel{left:156px;top:320px;width:472px;height:104px;background:var(--yellow);box-shadow:0 10px 18px rgba(0,0,0,.18)}
  .welcome-title{left:0;top:352px;width:796px;text-align:center;font-size:16.3px;font-weight:700;color:#222}
  .welcome-sub{left:0;top:373px;width:796px;text-align:center;font-size:11.5px;color:#222}
  .welcome-tag{left:0;top:393px;width:796px;text-align:center;font-size:7px;letter-spacing:.6px;color:#222}

  .strengths-intro{left:123px;top:484px;font-size:9px}
  .strengths-title{left:123px;top:496px;font-size:13px;font-weight:700;color:var(--blue)}
  .strengths-text{left:123px;top:518px;font-size:7.2px}
  .expect-title{left:123px;top:550px;font-size:7.5px;font-weight:700}
  .service-list{left:123px;top:570px;list-style:none;font-size:7.2px}
  .service-list li{height:15.4px;display:flex;align-items:center;gap:5px}
  .service-list li::before{content:"";width:2.5px;height:2.5px;background:var(--blue)}
  .container-photo{left:282px;top:553px;width:395px;height:124px;
    background:radial-gradient(ellipse at 60% 50%,#a9c9e4 0%,#c8dcee 40%,#eef3f8 70%,#ffffff 100%)}

  .quality{left:0;top:734px;width:796px;height:261px;background:var(--yellow)}
  .quality-title{left:0;top:781px;width:796px;text-align:center;font-size:13px;font-weight:700}
  .quality-card{top:815px;width:172px;height:127px;background:var(--white);border-radius:4px;box-shadow:0 2px 8px rgba(0,0,0,.12);text-align:center;font-size:7.2px;line-height:10.5px}
  .quality-card svg{display:block;margin:29px auto 7px;width:26px;height:26px;fill:none;stroke:#333;stroke-width:1.2}

  .contact{left:0;top:1038px;width:796px;text-align:center;font-size:7.2px;line-height:10.5px}
  .contact h2{font-size:7.5px;font-weight:700;margin-bottom:10px}
  .contact p{margin-bottom:10px}

  .site-footer{left:0;top:1180px;width:796px;height:20px;background:var(--footer);color:var(--white);font-size:6.3px;display:flex;align-items:center;justify-content:center}
</style>
</head>
<body>

<header class="site-header abs"></header>
<div class="brand abs">
  <div class="brand-square"></div>
  <div class="brand-name">Metall- und Stahlbau Harkenfeld GmbH</div>
</div>
<div class="brand-claim abs">Meisterbetrieb der Innung seit 1965</div>
<nav class="main-nav abs">
  <span class="active">Home</span><span>·</span>
  <span>Leistungen</span><span>·</span>
  <span>Referenzen</span><span>·</span>
  <span>Stellenangebote</span><span>·</span>
  <span>aktuelle Meldungen</span><span>·</span>
  <span>Download</span><span>·</span>
  <span>Unternehmensvorstellung</span>
</nav>
<div class="nav-marker abs"></div>

<div class="hero abs" role="img" aria-label="Luftaufnahme einer Stahlhalle im Bau mit Dachpaneelen und sandigem Baugelände"></div>

<div class="contact-pill abs" style="left:216px;width:93px">
  <svg viewBox="0 0 24 24"><path d="M6.6 10.8a15 15 0 0 0 6.6 6.6l2.2-2.2a1 1 0 0 1 1-.25 11.4 11.4 0 0 0 3.6.6 1 1 0 0 1 1 1V20a1 1 0 0 1-1 1A17 17 0 0 1 3 4a1 1 0 0 1 1-1h3.5a1 1 0 0 1 1 1c0 1.25.2 2.45.6 3.6a1 1 0 0 1-.25 1z"/></svg>
  037346 5820
</div>
<div class="contact-pill abs" style="left:312px;width:166px">
  <svg viewBox="0 0 24 24"><path d="M2 5h20v2l-10 7L2 7zm0 4.5l10 7 10-7V19H2z"/></svg>
  stahlbau.harkenfeld@beispielpost.de
</div>
<div class="contact-pill abs" style="left:486px;width:92px">
  <svg viewBox="0 0 24 24"><path d="M3 8h3v13H3zM8 3h10v6H8zM8 10h13v11H8zm3 3v2h2v-2zm4 0v2h2v-2zm-4 4v2h2v-2zm4 0v2h2v-2z"/></svg>
  037346 5821
</div>

<div class="welcome-panel abs" role="img" aria-label="Dekoratives gelb-blaues Begrüßungsband"></div>
<div class="welcome-title abs">Wir begrüßen Sie recht herzlich auf unseren Seiten.</div>
<div class="welcome-sub abs">Metall- und Stahlbau Harkenfeld GmbH</div>
<div class="welcome-tag abs">Firmenverbund Strahlenschutzbau</div>

<div class="strengths-intro abs">Unsere Stärken sind</div>
<h1 class="strengths-title abs">Kompetenz, Qualität und Zuverlässigkeit.</h1>
<p class="strengths-text abs">Qualifizierte Mitarbeiter und eine moderne Fertigung erfüllen höchste Qualitätsanforderungen.</p>
<h2 class="expect-title abs">Sie können von uns erwarten:</h2>
<ul class="service-list abs">
  <li>Beratung, Planung und Konstruktion</li>
  <li>Metall- und Stahlbau</li>
  <li>Blechbearbeitung</li>
  <li>Fertigung und Montage</li>
  <li>Wartung und Instandhaltung</li>
  <li>kundenspezifische Sonderanfertigungen</li>
  <li>Strahlenschutzbau</li>
</ul>
<div class="container-photo abs" role="img" aria-label="Hellblaue Bürocontaineranlage mit Fenstern"></div>

<section class="quality abs"></section>
<h2 class="quality-title abs">Qualitätssicherungssystem:</h2>
<div class="quality-card abs" style="left:123px">
  <svg viewBox="0 0 26 26"><path d="M6 2h11l4 4v18H6z"/><circle cx="13.5" cy="10" r="3"/><path d="M9 16h9M9 19h9M9 22h9"/></svg>
  Zertifizierung für Tragende Bauteile<br>und Bausätze für Stahltragwerke bis<br>EXC2 nach EN 1090-2
</div>
<div class="quality-card abs" style="left:312px">
  <svg viewBox="0 0 26 26"><path d="M13 3v5M13 18v5M3 13h5M18 13h5M6 6l3.5 3.5M16.5 16.5L20 20M20 6l-3.5 3.5M9.5 16.5L6 20"/><circle cx="13" cy="13" r="2.5"/></svg>
  Schweißzertifikat nach<br>EN 1090-2:2008+A1:2011, Ausführungsklasse<br>EXC2 nach EN 1090-2
</div>
<div class="quality-card abs" style="left:501px">
  <svg viewBox="0 0 26 26"><path d="M4 3h14v20H4z"/><path d="M7 8l1.5 1.5L11 7M7 13l1.5 1.5L11 12M7 18l1.5 1.5L11 17M13 8h3M13 13h3M13 18h2"/><circle cx="20" cy="17" r="3.5"/></svg>
  Zertifizierung zu<br>Qualitätssicherungssystem,<br>DIN EN ISO 3834-3
</div>

<section class="contact abs">
  <h2>Kontakt</h2>
  <p>Metall- und Stahlbau Harkenfeld GmbH<br>Talstraße 14<br>09471 Birkenhain</p>
  <p>Tel.: 037346 5820<br>Fax: 037346 5821</p>
  <p>stahlbau.harkenfeld@beispielpost.de</p>
</section>

<footer class="site-footer abs">© Metall- und Stahlbau Harkenfeld GmbH</footer>

</body>
</html>
```